New Business Card Design Project

I would like my card design to look exactly like the logo, design, layout, and print of the current attached file. The only change I would like made would be for the print to say THE KMW GROUP instead of THE HALLORAN GROUP. Basically, just replace his group name with my group name. I would also like the backgroud to be the same texture and color as the attached file. I love the dark blue lettering and house logo on the card.

I am completely open to the rest of the card design. I just want something clean and simple. Only basic contact info required on the card. Maybe just name: Kyle M Warrick and cell # 555.914.2087 and email kyle@orchidhomesagent.com

```html
<!DOCTYPE html>
<html lang="en">
<head>
<meta charset="utf-8">
<title>The KMW Group – Business Card</title>
<link rel="stylesheet" href="https://fonts.googleapis.com/css2?family=Open+Sans:wght@400;700&display=swap">
<style>
  :root {
    --navy: #2a2a6e;
    --paper: #eeeff2;
    --paper-edge: #e2e3e8;
    --lilac: #c9c9da;
    --backdrop: #2b2b2d;
  }
  * { box-sizing: border-box; margin: 0; padding: 0; }
  html, body {
    width: 1200px; height: 1200px; overflow: hidden;
    background: var(--backdrop);
    font-family: "Open Sans", sans-serif;
    color: var(--navy);
  }
  .stage { position: relative; width: 1200px; height: 1200px; }
  .card {
    position: absolute; left: 250px; width: 700px; height: 400px;
    background: radial-gradient(ellipse at 40% 40%, #f6f6f8 0%, var(--paper) 55%, var(--paper-edge) 100%);
    overflow: hidden;
  }
  .card--contact { top: 150px; }
  .card--brand { top: 650px; }

  .contact__accent {
    position: absolute; right: 0; top: 0; width: 300px; height: 230px;
    background: radial-gradient(ellipse at 80% 20%, var(--lilac) 0%, rgba(201,201,218,0.55) 45%, rgba(201,201,218,0) 75%);
  }
  .contact__name {
    position: absolute; left: 50px; top: 110px;
    font-weight: 700; font-size: 34px; letter-spacing: 0.32em;
    text-transform: uppercase; white-space: nowrap;
  }

  .lockup {
    display: flex; align-items: center;
    border: 3px solid var(--navy); border-radius: 14px;
    padding: 14px 18px; gap: 14px;
  }
  .lockup__square { width: 46px; height: 46px; background: var(--navy); flex: none; }
  .lockup__divider { width: 2px; align-self: stretch; background: var(--navy); flex: none; }
  .lockup__name {
    font-weight: 400; font-size: 20px; letter-spacing: 0.14em; line-height: 1.05;
    text-transform: uppercase; white-space: nowrap;
  }
  .card--contact .lockup { position: absolute; left: 50px; top: 240px; }

  .contact__details {
    position: absolute; left: 310px; top: 236px;
    list-style: none; font-size: 20px; letter-spacing: 0.08em;
  }
  .contact__details li {
    display: flex; align-items: center; gap: 10px; margin-bottom: 14px; white-space: nowrap;
  }
  .contact__details svg { width: 20px; height: 20px; fill: var(--navy); flex: none; }

  .card--brand .lockup {
    position: absolute; left: 50%; top: 50%; transform: translate(-50%, -50%);
    border-width: 4px; border-radius: 22px; padding: 34px 60px; gap: 30px;
  }
  .card--brand .lockup__square { width: 110px; height: 110px; }
  .card--brand .lockup__divider { width: 3px; }
  .card--brand .lockup__name { font-size: 40px; }
</style>
</head>
<body>
<main class="stage">
  <section class="card card--contact">
    <div class="contact__accent" role="img" aria-label="Soft lilac abstract shapes in the top corner"></div>
    <h1 class="contact__name">Kyle M Warrick</h1>
    <div class="lockup">
      <span class="lockup__square"></span>
      <span class="lockup__divider"></span>
      <span class="lockup__name">The<br>KMW<br>Group</span>
    </div>
    <ul class="contact__details">
      <li>
        <svg viewBox="0 0 24 24" aria-hidden="true"><path d="M6.6 10.8a15.1 15.1 0 0 0 6.6 6.6l2.2-2.2c.3-.3.7-.4 1-.2 1.1.4 2.3.6 3.6.6.6 0 1 .4 1 1V20c0 .6-.4 1-1 1A17 17 0 0 1 3 4c0-.6.4-1 1-1h3.5c.6 0 1 .4 1 1 0 1.3.2 2.5.6 3.6.1.3 0 .7-.2 1z"/></svg>
        <span>555.914.2087</span>
      </li>
      <li>
        <svg viewBox="0 0 24 24" aria-hidden="true"><path d="M2 5h20v14H2z"/><path d="M2.5 5.5l9.5 7.5 9.5-7.5" fill="none" stroke="#eeeff2" stroke-width="1.4"/></svg>
        <span>kyle@orchidhomesagent.com</span>
      </li>
    </ul>
  </section>

  <section class="card card--brand">
    <div class="lockup">
      <span class="lockup__square"></span>
      <span class="lockup__divider"></span>
      <span class="lockup__name">The<br>KMW<br>Group</span>
    </div>
  </section>
</main>
</body>
</html>
```